Harlow Auto , a Dealership and Repair Shop in Marengo Iowa

Harlow Auto is a repair shop and auto sales dealership that offers oil changes, alignments, tires, air conditioning work, computer diagnostics. Focused on Vantras, Marlo and Brisk. Small business with less than 10 employees. Billboard sign is in town and not the larger billboard
billboard is 8ft x 18ft

Target Market(s)

General public

Industry/Entity Type

automotive

Font styles to use
Serif
Sans Serif

Colors

Designer to choose colors to be used in the design.

Requirements
Must have
• Located 2 miles north of Marengo. Sales and service. Phone number 319-555-0187
Nice to have
• Picture of a car or truck, or both. picture of wrench
Should not have
• Not sure

```html
<!DOCTYPE html>
<html lang="en">
<head>
<meta charset="utf-8">
<title>Harlow Auto — Billboard</title>
<link href="https://fonts.googleapis.com/css2?family=Exo+2:wght@600;700&display=swap" rel="stylesheet">
<style>
  :root {
    --page-bg: #ecebe8;
    --board-blue: #0a3db0;
    --board-blue-deep: #0837a3;
    --scene-navy: #1c2d6b;
    --scene-dusk: #5d6a9a;
    --scene-road: #1e2638;
    --vehicle-white: #e9ecf2;
    --text-white: #ffffff;
    --accent-yellow: #ffcb05;
  }
  * { margin: 0; padding: 0; box-sizing: border-box; }
  html, body {
    width: 1200px;
    height: 900px;
    overflow: hidden;
    background: var(--page-bg);
  }
  .billboard {
    position: absolute;
    left: 40px;
    top: 192px;
    width: 1120px;
    height: 516px;
    background: var(--board-blue);
    overflow: hidden;
    font-family: "Exo 2", "Arial", sans-serif;
    font-weight: 700;
    color: var(--text-white);
  }
  .vehicle-scene {
    position: absolute;
    left: 560px;
    top: 0;
    width: 560px;
    height: 516px;
    background:
      radial-gradient(ellipse 60% 38% at 58% 72%, var(--vehicle-white) 0%, rgba(233,236,242,0.85) 45%, rgba(233,236,242,0) 75%),
      linear-gradient(180deg, rgba(10,61,176,0) 0%, var(--scene-dusk) 40%, var(--scene-navy) 62%, var(--scene-road) 100%);
    -webkit-mask-image: linear-gradient(90deg, transparent 0%, #000 32%);
            mask-image: linear-gradient(90deg, transparent 0%, #000 32%);
  }
  .brand {
    position: absolute;
    left: 24px;
    top: 70px;
  }
  .brand-name {
    font-size: 64px;
    line-height: 1;
    color: var(--text-white);
    letter-spacing: 0.5px;
  }
  .brand-town {
    margin-top: 10px;
    font-size: 20px;
    font-weight: 600;
    letter-spacing: 1px;
    padding-left: 4px;
  }
  .phone {
    position: absolute;
    right: 32px;
    top: 48px;
    display: flex;
    align-items: center;
    gap: 16px;
    font-size: 46px;
    font-weight: 600;
    line-height: 1;
  }
  .phone-icon { width: 38px; height: 38px; flex: none; }
  .headline {
    position: absolute;
    left: 22px;
    font-size: 51px;
    line-height: 1;
    letter-spacing: 0.5px;
  }
  .headline--distance { top: 248px; color: var(--accent-yellow); }
  .headline--place { top: 318px; color: var(--text-white); }
  .tagline {
    position: absolute;
    left: 22px;
    top: 422px;
    font-size: 44px;
    line-height: 1;
    color: var(--accent-yellow);
    letter-spacing: 1px;
  }
</style>
</head>
<body>
  <main class="billboard">
    <div class="vehicle-scene" role="img" aria-label="Photo of a white station wagon parked in front of a semi truck at dusk"></div>

    <div class="brand">
      <div class="brand-name">Harlow Auto</div>
      <div class="brand-town">Marengo, IA</div>
    </div>

    <div class="phone">
      <svg class="phone-icon" viewBox="0 0 40 40" aria-hidden="true">
        <rect width="40" height="40" rx="7" fill="#ffffff"/>
        <path d="M13.5 9.5c1-.6 2.2-.3 2.8.7l2 3.5c.5.9.3 2-.5 2.6l-1.6 1.2c1 2.4 2.9 4.4 5.3 5.5l1.3-1.6c.6-.8 1.8-1 2.6-.4l3.4 2.2c1 .6 1.2 1.9.6 2.8l-1.4 2c-.9 1.3-2.5 1.9-4 1.4C17.5 27.3 12.6 22.4 10.5 16c-.5-1.5.1-3.1 1.4-4z" fill="#0a3db0"/>
      </svg>
      <span>319-555-0187</span>
    </div>

    <p class="headline headline--distance">LOCATED 2 MILES</p>
    <p class="headline headline--place">NORTH OF MARENGO</p>
    <p class="tagline">SALES AND SERVICE</p>
  </main>
</body>
</html>
```